Building restoration company expanding services

We need a flyer to promote our new 'Commercial Cleaning" and 'Property Maintenance' Services to new and existing customers.
We want to use our current logo and colours and add our new catch phrase, 'Restore, Repair and Maintain' instead of 'building a healthy future' These 2 new services can be in new colours to flow with the 'air, fire, flood and mould' such as a yellow and purple perhaps.
We are offering a free 'Moisture Inspection' valued at $199 once a year. this will prevent any costly building repairs as a result of pipes leaking etc
Our website has more detailed information www.kelvardholdings.net
We would like people to know we are trusted, professionals from working in the industry for over 16 years.
We are providing these extra services due to our current customers requests. Due to our background we can provide repairs or restoration to almost anything and by maintaining many costly replacements or repairs are avoided.

Target Market(s)

Corporate Businesses
Builders

Industry/Entity Type

It Company

Requirements
Must have
• Contact details
• Our colours
• Logo
Nice to have
• Images to reflect our professional and trusted company.

```html
<!DOCTYPE html>
<html lang="en">
<head>
<meta charset="utf-8">
<title>Kelvard Holdings – Restore, Repair &amp; Maintain Flyer</title>
<link rel="stylesheet" href="https://fonts.googleapis.com/css2?family=Bebas+Neue&family=Lato:ital,wght@0,400;0,700;1,700&display=swap">
<style>
  :root {
    --lime: #8cc63f;
    --lime-bright: #97d11f;
    --charcoal: #3a3b3d;
    --grey-logo: #5e5f61;
    --paper: #ffffff;
    --mist: #eef0ef;
    --backdrop: #f2f2f2;
    --ink: #222222;
  }
  * { margin: 0; padding: 0; box-sizing: border-box; }
  html, body { width: 1200px; height: 1200px; overflow: hidden; background: var(--backdrop); }
  .flyer {
    position: absolute; left: 200px; top: 50px;
    width: 800px; height: 1100px;
    background: linear-gradient(180deg, var(--paper) 0%, var(--mist) 60%, var(--paper) 100%);
    overflow: hidden;
    box-shadow: 0 6px 24px rgba(0,0,0,.18);
  }
  .flyer-shapes { position: absolute; inset: 0; width: 800px; height: 1100px; }
  .brand {
    position: absolute; right: 70px; top: 48px;
    font-family: 'Lato', sans-serif; font-weight: 700;
    color: var(--grey-logo); text-align: right;
    font-size: 44px; line-height: 1; letter-spacing: 1px;
  }
  .brand small { display: block; font-size: 22px; letter-spacing: 6px; margin-top: 8px; }
  .tagline {
    position: absolute; right: 78px; top: 186px;
    font-family: 'Bebas Neue', sans-serif; font-size: 56px; line-height: 48px;
    text-align: right; color: var(--paper);
  }
  .tagline .dark { color: var(--charcoal); }
  .offer {
    position: absolute; left: 60px; top: 500px; width: 305px;
    font-family: 'Bebas Neue', sans-serif; text-align: center; line-height: 1;
  }
  .offer-free { font-size: 150px; color: var(--lime-bright); line-height: 120px; }
  .offer-item { font-size: 34px; color: var(--paper); margin-top: 6px; }
  .offer-price { font-size: 96px; color: var(--lime-bright); line-height: 82px; }
  .offer-period { font-size: 58px; color: var(--paper); line-height: 56px; }
  .expertise-title {
    position: absolute; left: 512px; top: 530px;
    font-family: 'Lato', sans-serif; font-style: italic; font-weight: 700;
    font-size: 28px; color: var(--paper);
  }
  .expertise-list {
    position: absolute; right: 34px; top: 584px; width: 470px;
    list-style: none; font-family: 'Lato', sans-serif; font-size: 18.5px;
    line-height: 23px; color: var(--ink); text-align: right;
  }
  .expertise-list li { position: relative; padding-right: 22px; }
  .expertise-list li::after {
    content: ""; position: absolute; right: 0; top: 8px;
    width: 9px; height: 9px; border-radius: 50%; background: var(--lime);
  }
  .expertise-list .note::after { display: none; }
  .expertise-list .new { font-weight: 700; }
  .contact {
    position: absolute; right: 44px; top: 985px;
    font-family: 'Lato', sans-serif; font-weight: 700; font-size: 24px;
    line-height: 30px; color: var(--paper); text-align: right;
  }
</style>
</head>
<body>
<div class="flyer">
  <svg class="flyer-shapes" viewBox="0 0 800 1100" xmlns="http://www.w3.org/2000/svg">
    <defs>
      <linearGradient id="familyTone" x1="0" y1="0" x2="1" y2="1">
        <stop offset="0" stop-color="#dfe6d0"/>
        <stop offset="0.5" stop-color="#e8c9b4"/>
        <stop offset="1" stop-color="#c9cfd6"/>
      </linearGradient>
      <linearGradient id="equipTone" x1="0" y1="0" x2="0" y2="1">
        <stop offset="0" stop-color="#b98b62"/>
        <stop offset="1" stop-color="#9fb1c2"/>
      </linearGradient>
    </defs>
    <polygon points="0,0 352,0 478,200 512,440 380,490 0,380" fill="url(#familyTone)" role="img" aria-label="Photo of a smiling family of four"/>
    <polygon points="352,0 378,0 500,198 534,436 512,440 478,200" fill="var(--charcoal)"/>
    <polygon points="378,0 800,0 800,350 534,436 500,198" fill="var(--lime-bright)"/>
    <polygon points="0,380 0,400 90,436 96,420" fill="var(--charcoal)"/>
    <polygon points="365,505 800,358 800,384 365,530" fill="var(--charcoal)"/>
    <polygon points="0,1050 800,862 800,876 0,1064" fill="var(--charcoal)"/>
    <polygon points="0,1076 800,888 800,1100 0,1100" fill="var(--lime-bright)"/>
    <polygon points="60,478 212,420 365,478 365,1010 60,1040" fill="var(--lime-bright)"/>
    <polygon points="66,484 212,428 359,484 359,1000 66,1030" fill="var(--charcoal)"/>
    <path d="M516,526 H790 V574 H516 A24,24 0 0 1 516,526 Z" fill="var(--lime-bright)" stroke="var(--charcoal)" stroke-width="2"/>
    <circle cx="214" cy="956" r="106" fill="var(--paper)"/>
    <circle cx="214" cy="956" r="94" fill="var(--lime-bright)"/>
    <circle cx="214" cy="956" r="86" fill="url(#equipTone)" role="img" aria-label="Photo of a drying fan with ducting on a concrete floor"/>
  </svg>

  <div class="brand">KELVARD<small>HOLDINGS</small></div>

  <div class="tagline">
    <div>Restore</div>
    <div class="dark">Repair &amp;</div>
    <div>Maintain</div>
  </div>

  <div class="offer">
    <div class="offer-free">Free</div>
    <div class="offer-item">Moisture Inspection</div>
    <div class="offer-price">At $199</div>
    <div class="offer-period">Once a Year</div>
  </div>

  <div class="expertise-title">Our core expertise</div>
  <ul class="expertise-list">
    <li class="new">NEW: Commercial Cleaning</li>
    <li class="new">NEW: Property Maintenance</li>
    <li>Flood and Fire damage remediation</li>
    <li class="note">(contents &amp; structural)</li>
    <li>Thermal Imaging Infra-Red moisture</li>
    <li class="note">and damp building inspections</li>
    <li>Mould Remediation</li>
    <li>Indoor Air Quality Issues</li>
    <li>Damp and Moisture Problems</li>
    <li>Severe odour problems</li>
    <li>Sub-Floor Ventilation</li>
    <li>Contents restoration (limited)</li>
  </ul>

  <div class="contact">
    <div>Ph: 4820 3317</div>
    <div>admin@kelvardholdings.net</div>
    <div>www.kelvardholdings.net</div>
  </div>
</div>
</body>
</html>
```